Box and label design for oil Tincture bottle

I need to design an attractive looking label for a 30ml CBD oil tincture along with designing a box for the tincture oil. I already have the logo (see attachment). I just need a nice, attractive looking artwork for the label and the box. The box is the standard 30ml tincture oil (see example attachment). The box has a total of 6 sides (4 on sides and 2 for top and bottom). Please include a section for supplemental facts and ingredients. Let's not focus to much on content. I am more concerned with design of box and label.
Target Market(s)
CBD customers
Look and feel
Each slider illustrates characteristics of the customer's brand and the style your logo design should communicate.

```html
<!DOCTYPE html>
<html lang="en">
<head>
<meta charset="utf-8">
<title>Bright Harvest CBD – Tincture Box and Labels</title>
<link href="https://fonts.googleapis.com/css2?family=Oswald:wght@400;500;600&family=Roboto+Condensed:wght@400;700&display=swap" rel="stylesheet">
<style>
  :root{
    --bg:#8792b0;
    --red:#a3191e;
    --red-dark:#86161a;
    --blue:#1f78c1;
    --blue-light:#4fb3e8;
    --navy:#263a8c;
    --paper:#eef1f5;
    --white:#ffffff;
  }
  *{box-sizing:border-box;margin:0;padding:0}
  html,body{width:1200px;height:1200px;overflow:hidden;background:var(--bg)}
  body{position:relative;font-family:"Roboto Condensed",sans-serif}
  .panel{position:absolute;overflow:hidden}
  .brand{font-family:"Oswald",sans-serif;font-weight:600;line-height:1;letter-spacing:-0.5px;text-align:center;text-transform:uppercase;white-space:nowrap}
  .brand-sub{font-family:"Oswald",sans-serif;font-weight:400;display:flex;align-items:center;justify-content:center;gap:8px;text-transform:uppercase;line-height:1}
  .brand-sub::before,.brand-sub::after{content:"";height:1.5px;flex:1;background:currentColor}
  .mark-dot{border-radius:50%;margin:0 auto}

  /* side panel */
  .box-side{left:50px;top:60px;width:310px;height:800px;background:linear-gradient(160deg,#b22328,var(--red-dark));color:var(--white)}
  .box-side .mark-dot{width:44px;height:44px;border:3px solid var(--white);margin-top:30px}
  .box-side .brand{font-size:28px;margin-top:10px;color:var(--white)}
  .box-side .brand-sub{font-size:13px;width:150px;margin:2px auto 0}
  .facts{margin:18px auto 0;width:250px;background:var(--white);color:var(--navy);padding:7px 9px;font-size:8.5px;line-height:1.25;border:2px solid var(--navy)}
  .facts h3{font-family:"Roboto Condensed",sans-serif;font-weight:700;font-size:22px;line-height:1}
  .facts .rule-thick{height:5px;background:var(--navy);margin:3px 0}
  .facts .row{display:flex;justify-content:space-between;border-bottom:1px solid #9aa3c4;padding:1px 0}
  .facts .row.ind{padding-left:10px}
  .facts .note{font-size:7px;margin-top:3px;line-height:1.3}
  .side-heading{font-family:"Oswald",sans-serif;font-weight:400;font-size:15px;text-align:center;margin:20px auto 0;width:210px;padding-bottom:4px;border-bottom:3px solid var(--white)}
  .side-copy{width:210px;margin:9px auto 0;font-size:12px;line-height:1.4;text-align:justify}
  .side-circle{position:absolute;left:170px;bottom:-110px;width:220px;height:220px;border-radius:50%;background:var(--white);border:12px solid var(--navy)}
  .site{position:absolute;left:10px;bottom:10px;font-size:12px}

  /* front panel */
  .box-front{left:360px;top:60px;width:300px;height:800px;background:var(--red-dark);color:var(--navy)}
  .box-front svg.shape{position:absolute;inset:0}
  .box-front .abs{position:absolute;left:0;right:0;text-align:center}
  .front-infused{top:42px;color:var(--white);font-family:"Oswald",sans-serif;font-size:13px;letter-spacing:1px;line-height:1.3}
  .tag-outline{display:inline-block;border:2px solid var(--navy);padding:2px 10px;font-family:"Oswald",sans-serif;font-size:17px;color:var(--navy)}
  .front-spec{top:232px}
  .box-front .mark-dot{position:absolute;left:102px;top:300px;width:96px;height:96px;border:4px solid var(--navy)}
  .box-front .brand{top:420px;font-size:38px;color:var(--navy)}
  .box-front .brand-sub{position:absolute;left:25px;right:25px;top:466px;font-size:22px;color:var(--navy)}
  .tag-bar{top:556px;margin:0 auto;width:180px;background:var(--blue);color:var(--white);font-family:"Oswald",sans-serif;font-size:20px;padding:2px 0}
  .front-dose{top:596px;margin:0 auto;width:160px;font-family:"Oswald",sans-serif;font-size:30px;line-height:1.2;padding:4px 0;border-top:1px solid var(--navy);border-bottom:1px solid var(--navy)}
  .vol-dot{position:absolute;display:flex;align-items:center;justify-content:center;border-radius:50%;background:var(--navy);color:var(--white);font-size:10px}
  .box-front .vol-dot{right:22px;bottom:30px;width:36px;height:36px}

  /* labels */
  .label{left:700px;width:450px;height:500px;background:var(--paper);color:var(--navy);text-align:center}
  .label-a{top:60px}
  .label-b{top:600px;height:520px}
  .label .mark-dot{width:84px;height:84px;border:4px solid var(--navy)}
  .label .brand{font-size:42px;color:var(--navy)}
  .label .brand-sub{font-size:20px;width:280px;margin:3px auto 0}
  .label-a .top-band{height:8px;background:var(--red)}
  .label-a .mark-dot{margin-top:28px}
  .label-a .brand{margin-top:14px}
  .label-a .lower{position:absolute;left:0;right:0;top:330px;bottom:0;background:var(--red)}
  .label-a .blue-band{position:absolute;left:0;right:0;top:310px;height:34px;background:var(--blue)}
  .quality-box{position:absolute;left:95px;top:212px;width:260px;height:212px;background:var(--white);border:3px solid var(--navy);border-radius:14px}
  .quality-top{display:inline-block;background:var(--navy);color:var(--white);font-size:10px;letter-spacing:1px;padding:2px 16px;margin-top:-1px;font-weight:700}
  .quality-spec{font-family:"Oswald",sans-serif;font-size:15px;letter-spacing:1px;margin-top:10px}
  .quality-name{font-family:"Oswald",sans-serif;font-weight:600;font-size:40px;color:var(--blue);line-height:1.1}
  .quality-dose{position:absolute;left:-3px;right:-3px;top:96px;height:34px;background:var(--blue);color:var(--white);font-family:"Oswald",sans-serif;font-size:24px;line-height:34px}
  .quality-infused{position:absolute;left:0;right:0;bottom:22px;color:var(--blue);font-size:11px;letter-spacing:1px}
  .label-a .vol-dot{left:207px;bottom:18px;width:36px;height:36px}

  .label-b .top-band{height:34px;background:var(--red);color:var(--white);font-family:"Oswald",sans-serif;font-size:15px;line-height:34px;letter-spacing:.5px}
  .label-b svg.chevrons{display:block}
  .label-b .mark-dot{margin-top:8px}
  .label-b .brand{margin-top:14px}
  .label-b .infused{width:300px;margin:26px auto 0;padding:6px 0;border-top:1.5px solid var(--red);border-bottom:1.5px solid var(--red);font-size:12px;letter-spacing:1px}
  .label-b .dose-tag{display:inline-block;background:var(--red);color:var(--white);font-family:"Oswald",sans-serif;font-size:20px;padding:1px 30px;clip-path:polygon(0 0,100% 0,92% 100%,8% 100%)}
  .label-b .vol-dot{left:207px;bottom:40px;width:36px;height:36px}
  .label-b .bottom-band{position:absolute;left:0;right:0;bottom:0;height:14px;background:var(--blue)}
</style>
</head>
<body>

<section class="panel box-side">
  <div class="mark-dot"></div>
  <div class="brand">Bright Harvest</div>
  <div class="brand-sub">CBD</div>
  <div class="facts">
    <h3>Supplement Facts</h3>
    <div>Serving Size 1 Capsule<br>Servings Per Container 100</div>
    <div class="rule-thick"></div>
    <div class="row"><b>Amount Per Capsule</b><span>% Daily Value</span></div>
    <div class="row"><span>Calories 20</span><span></span></div>
    <div class="row"><span>Total Fat 2 g</span><span>3%*</span></div>
    <div class="row ind"><span>Saturated Fat 0.5 g</span><span>3%*</span></div>
    <div class="row ind"><span>Polyunsaturated Fat 1 g</span><span>†</span></div>
    <div class="row ind"><span>Monounsaturated Fat 0.5 g</span><span>†</span></div>
    <div class="row"><span>Vitamin A 765 mcg</span><span>85%</span></div>
    <div class="row"><span>Vitamin D 21 mcg</span><span>105%</span></div>
    <div class="rule-thick"></div>
    <div class="row"><span>Omega-3 fatty acids 0.5 g</span><span>†</span></div>
    <div class="rule-thick"></div>
    <div class="note">* Percent Daily Values are based on a 2,000 calorie diet.<br>† Daily Value not established.</div>
  </div>
  <h4 class="side-heading">INGREDIENTS</h4>
  <p class="side-copy">Rum sincia preium cuptatenim la sum res dolorum alitas plique reium quis et, odigenihit rem facere ne voluptatque</p>
  <h4 class="side-heading">DIRECTIONS OF USE</h4>
  <p class="side-copy">Officitem intistis demporate doloriasita nullata turiaecum haris voluptiae volorectem ant quatur, coreius mi, suntiumque reium nonet auditatus velestiam escipid quo min plabo.</p>
  <div class="side-circle"></div>
  <div class="site">BrightHarvestCBD.com</div>
</section>

<section class="panel box-front">
  <svg class="shape" width="300" height="800" viewBox="0 0 300 800" aria-hidden="true">
    <polygon points="0,180 300,140 300,700 0,650" fill="var(--blue)"/>
    <polygon points="0,200 300,170 300,675 0,635" fill="var(--paper)"/>
    <polygon points="0,180 300,140 0,200" fill="var(--red-dark)"/>
    <polygon points="0,650 300,700 0,635" fill="var(--red-dark)"/>
  </svg>
  <div class="abs front-infused">INFUSED WITH<br>RICH CANNABINOIDS</div>
  <div class="abs front-spec"><span class="tag-outline">FULL SPECTRUM</span></div>
  <div class="mark-dot"></div>
  <div class="abs brand">Bright Harvest</div>
  <div class="brand-sub">CBD</div>
  <div class="abs tag-bar">TINCTURE</div>
  <div class="abs front-dose">250MG</div>
  <div class="vol-dot">50ml</div>
</section>

<section class="panel label label-a">
  <div class="top-band"></div>
  <div class="mark-dot"></div>
  <div class="brand">Bright Harvest</div>
  <div class="brand-sub">CBD</div>
  <div class="lower"></div>
  <div class="blue-band"></div>
  <div class="quality-box">
    <span class="quality-top">PREMIUM QUALITY</span>
    <div class="quality-spec">FULL SPECTRUM</div>
    <div class="quality-name">TINCTURE</div>
    <div class="quality-dose">250MG</div>
    <div class="quality-infused">INFUSED WITH RICH CANNABINOIDS</div>
  </div>
  <div class="vol-dot">50ml</div>
</section>

<section class="panel label label-b">
  <div class="top-band">TINCTURE</div>
  <svg class="chevrons" width="450" height="80" viewBox="0 0 450 80" aria-hidden="true">
    <polygon points="0,0 225,22 450,0 450,18 225,40 0,18" fill="var(--blue)"/>
    <polygon points="0,18 225,40 450,18 450,36 225,58 0,36" fill="#3a97d6"/>
    <polygon points="0,36 225,58 450,36 450,52 225,74 0,52" fill="var(--blue-light)"/>
  </svg>
  <div class="mark-dot"></div>
  <div class="brand">Bright Harvest</div>
  <div class="brand-sub">CBD</div>
  <div class="infused">INFUSED WITH RICH CANNABINOIDS</div>
  <span class="dose-tag">250MG</span>
  <div class="vol-dot">50ml</div>
  <div class="bottom-band"></div>
</section>

</body>
</html>
```